Nutrition product information web site

Nutrition Website (see upload) without Shop function but link to Velmora ASIN number that customer could order from Velmora direct. Content must be easily editable without coding. Web environment must be responsive to support mobile devices as well. design should be modern and clear. loading of web elements must be fast. not too much time consuming features.

Industry/Entity Type

Nutrition

Number of Pages Required

5+ page

Font styles to use
Sans Serif

Colors
33b8a4
9bcb3c
0255a3
0a90cc
a54499

Requirements
Must have
• read attached document
Nice to have
• read attached document
Should not have
• read attached document

```html
<!DOCTYPE html>
<html lang="en">
<head>
<meta charset="utf-8">
<title>Corvane – Product</title>
<link href="https://fonts.googleapis.com/css2?family=Raleway:wght@400;500;600;700&family=Roboto:wght@400;500&display=swap" rel="stylesheet">
<style>
:root{
  --teal:#17b8c4;
  --teal-dark:#12a3ae;
  --magenta:#a54499;
  --blue:#0255a3;
  --sky:#0a90cc;
  --ink:#1d1d1d;
  --grey-text:#8f8f8f;
  --panel:#e4e4e4;
  --white:#ffffff;
}
*{box-sizing:border-box;margin:0;padding:0}
html,body{width:1118px;height:1200px;overflow:hidden;background:var(--white)}
body{position:relative;font-family:'Raleway',sans-serif;color:var(--ink)}
.abs{position:absolute}

/* header */
.site-header{left:0;top:0;width:1118px;height:200px;
  background:linear-gradient(100deg,#ffffff 0%,#eefaff 25%,#d6f4fb 55%,#cdeafb 75%,#e6f7fd 100%)}
.brand{left:52px;top:18px;display:flex;flex-direction:column;align-items:center;gap:8px}
.brand-mark{width:70px;height:70px;border:4px solid var(--teal);border-radius:50%}
.brand-name{font-weight:700;font-size:34px;letter-spacing:4px;color:var(--ink)}
.lang-switch{left:920px;top:22px;display:flex;gap:9px}
.lang-switch svg{width:25px;height:25px}
.search-btn{left:1042px;top:65px;width:35px;height:35px;border-radius:50%;border:1px solid #b9dfe6;background:#eefbff;display:flex;align-items:center;justify-content:center}
.main-nav{left:772px;top:108px;display:flex;gap:26px;font-size:15px;font-weight:500;letter-spacing:.5px}
.main-nav a{color:var(--teal);text-decoration:none;position:relative}
.main-nav a.home{color:var(--grey-text)}
.main-nav a.current::after{content:"";position:absolute;left:0;right:0;bottom:-9px;height:2px;background:var(--magenta)}

/* product intro */
.product-title{left:0;width:1118px;top:237px;text-align:center;font-size:16px;font-weight:600;color:var(--magenta);letter-spacing:.4px}
.product-lead{left:348px;width:420px;top:299px;text-align:center;font-size:13px;line-height:14.5px;letter-spacing:.8px;color:#333}
.photo{border-radius:8px}
.photo-bottle{left:114px;top:313px;width:135px;height:227px;border-radius:10px;background:linear-gradient(90deg,#cfd3d6,#f7f8f9 45%,#dfe3e6)}
.photo-capsules{left:313px;top:416px;width:266px;height:115px;border-radius:50px;background:linear-gradient(90deg,#2c6fd1,#e9eef4 50%,#2c6fd1)}
.photo-herb{left:754px;top:403px;width:283px;height:171px;border-radius:60px;background:radial-gradient(ellipse at 55% 45%,#f1e045 0%,#8dbb3b 45%,rgba(255,255,255,0) 75%)}
.order-btn{left:121px;top:579px;width:120px;height:24px;border-radius:7px;background:var(--teal);color:var(--white);font-family:'Roboto',sans-serif;font-weight:500;font-size:13px;display:flex;align-items:center;justify-content:center}

/* info panel */
.info-panel{left:291px;top:584px;width:570px;height:296px;border:1px solid #a8a8a8;border-radius:4px;overflow:hidden;background:var(--panel);box-shadow:0 14px 16px -8px rgba(0,0,0,.35);font-family:'Roboto',sans-serif}
.info-heading{left:34px;top:44px;font-size:15px;font-weight:500;color:var(--blue)}
.info-text{left:10px;top:75px;width:257px;text-align:center;font-size:12px;line-height:19.3px;color:#333}
.benefit-list{left:278px;top:77px;list-style:none}
.benefit-list li{display:flex;align-items:center;gap:4px;height:47px;font-size:10.5px;color:#333}
.benefit-list li:first-child{height:auto;margin-bottom:34px}
.benefit-list svg{width:16px;height:16px;flex:none}
.tab-bar{left:0;top:222px;width:570px;height:74px;background:linear-gradient(#5c83ad 0,#3166a1 12%,#1d5ea3 60%,#17559a 100%);border-top:6px solid #3e5f80}
.tab-bar ul{list-style:none;display:flex;height:100%;padding-left:35px}
.tab-bar li{color:#e8f0f8;font-size:14px;font-weight:500;padding:0 12px;display:flex;align-items:center}
.tab-bar li.active{background:rgba(255,255,255,.2);position:relative;width:119px;justify-content:center;padding:0}
.tab-bar li.active::before{content:"";position:absolute;top:-1px;left:52px;border:9px solid transparent;border-top-color:#3e5f80}

/* footer */
.site-footer{left:0;top:1000px;width:1118px;height:200px;background:var(--teal);color:var(--white)}
.footer-brand{left:40px;top:47px;display:flex;flex-direction:column;align-items:center;gap:10px}
.footer-brand .brand-mark{width:70px;height:70px;border:3px solid #1d2b2d}
.footer-brand .brand-name{font-size:29px;color:#1d2b2d}
.footer-nav{left:397px;top:34px;display:flex;gap:15px;font-size:13.5px;font-weight:600;letter-spacing:.3px}
.company{left:830px;top:17px;width:262px;font-size:13px;letter-spacing:.5px}
.company-name{text-align:center;font-weight:700;margin-bottom:9px}
.contact-row{display:flex;align-items:flex-start;gap:10px;margin-left:8px}
.contact-row svg{flex:none;margin-top:2px}
.address{text-align:center;line-height:19.5px;width:214px}
.phone{margin-top:11px}
.email{margin-top:22px}
.copyright{left:0;width:1118px;top:1181px;display:flex;justify-content:center;align-items:center;gap:6px;font-size:10px;color:var(--white);letter-spacing:.3px}
</style>
</head>
<body>

<header class="site-header abs">
  <div class="brand abs"><span class="brand-mark"></span><span class="brand-name">CORVANE</span></div>

  <div class="lang-switch abs" aria-label="Language">
    <svg viewBox="0 0 24 24"><clipPath id="c1"><circle cx="12" cy="12" r="12"/></clipPath><g clip-path="url(#c1)"><rect width="24" height="24" fill="#1f3f8f"/><path d="M0 0L24 24M24 0L0 24" stroke="#fff" stroke-width="4"/><path d="M0 0L24 24M24 0L0 24" stroke="#cf2030" stroke-width="1.5"/><path d="M12 0V24M0 12H24" stroke="#fff" stroke-width="6"/><path d="M12 0V24M0 12H24" stroke="#cf2030" stroke-width="3.5"/></g></svg>
    <svg viewBox="0 0 24 24"><clipPath id="c2"><circle cx="12" cy="12" r="12"/></clipPath><g clip-path="url(#c2)"><rect width="24" height="24" fill="#c8102e"/><rect y="6" width="24" height="12" fill="#f5c400"/></g></svg>
    <svg viewBox="0 0 24 24"><clipPath id="c3"><circle cx="12" cy="12" r="12"/></clipPath><g clip-path="url(#c3)"><rect width="8" height="24" fill="#219148"/><rect x="8" width="8" height="24" fill="#fff"/><rect x="16" width="8" height="24" fill="#cf2b37"/></g></svg>
    <svg viewBox="0 0 24 24"><clipPath id="c4"><circle cx="12" cy="12" r="12"/></clipPath><g clip-path="url(#c4)"><rect width="24" height="8" fill="#111"/><rect y="8" width="24" height="8" fill="#d00"/><rect y="16" width="24" height="8" fill="#f5c400"/></g></svg>
    <svg viewBox="0 0 24 24"><clipPath id="c5"><circle cx="12" cy="12" r="12"/></clipPath><g clip-path="url(#c5)"><rect width="8" height="24" fill="#1f3f9f"/><rect x="8" width="8" height="24" fill="#fff"/><rect x="16" width="8" height="24" fill="#e02b37"/></g></svg>
  </div>

  <div class="search-btn abs" aria-label="Search">
    <svg width="22" height="22" viewBox="0 0 22 22"><circle cx="9" cy="9" r="6.5" fill="none" stroke="#17b8c4" stroke-width="2.5"/><path d="M13.5 13.5L19 19" stroke="#17b8c4" stroke-width="3.5" stroke-linecap="round"/></svg>
  </div>

  <nav class="main-nav abs">
    <a class="home" href="#">Home</a>
    <a class="current" href="#">Products</a>
    <a href="#">Blog</a>
    <a href="#">Contact Us</a>
  </nav>
</header>

<main>
  <h1 class="product-title abs">Lorem ipsum dolor sit amet</h1>
  <p class="product-lead abs">Lorem ipsum dolor sit amet, consectetuer adipiscing elit. Aenean commodo ligula eget dolor. Aenean massa. Cum sociis natoque penatibus et magnis dis parturient montes, nascetur ridiculus mus. Donec quam felis, ultricies nec, pellentesque eu, pretium quis, sem.</p>

  <div class="photo photo-bottle abs" role="img" aria-label="Product bottle of vitamin B complex capsules"></div>
  <div class="photo photo-capsules abs" role="img" aria-label="Blue and white capsules"></div>
  <div class="photo photo-herb abs" role="img" aria-label="Sprig of yellow flowering herb"></div>

  <a class="order-btn abs">ORDER</a>

  <section class="info-panel abs">
    <h2 class="info-heading abs">The power fruit for your health</h2>
    <p class="info-text abs">Lorem ipsum dolor sit amet, consectetuer adipiscing elit. Aenean commodo ligula eget dolor. Aenean massa. Cum sociis natoque penatibus et magnis dis parturient montes, nascetur ridiculus mus. Donec quam felis, ultricies nec, pellentesque eu, pretium quis, sem.</p>
    <ul class="benefit-list abs">
      <li><svg viewBox="0 0 16 16"><path d="M1 9l4 5L15 1" fill="none" stroke="#0a90cc" stroke-width="3"/></svg>Lorem ipsum dolor sit amet, consectetuer adipiscing elit.</li>
      <li><svg viewBox="0 0 16 16"><path d="M1 9l4 5L15 1" fill="none" stroke="#0a90cc" stroke-width="3"/></svg>Aenean commodo ligula eget dolor. Aenean massa.</li>
      <li><svg viewBox="0 0 16 16"><path d="M1 9l4 5L15 1" fill="none" stroke="#0a90cc" stroke-width="3"/></svg>In enim justo, rhoncus ut, imperdiet a, venenatis vitae, justo.</li>
    </ul>
    <nav class="tab-bar abs">
      <ul>
        <li class="active">Health benefits</li>
        <li>Ingredients</li>
        <li>Recommended use</li>
        <li>Reviews</li>
        <li>Facts</li>
      </ul>
    </nav>
  </section>
</main>

<footer class="site-footer abs">
  <div class="footer-brand brand abs"><span class="brand-mark"></span><span class="brand-name">CORVANE</span></div>
  <nav class="footer-nav abs"><span>Home</span><span>Blog</span><span>Products</span><span>About Us</span><span>Contact Us</span></nav>
  <div class="company abs">
    <p class="company-name">Lumeva Research GmbH</p>
    <div class="contact-row">
      <svg width="18" height="24" viewBox="0 0 18 24"><path d="M9 0a8 8 0 0 0-8 8c0 6 8 16 8 16s8-10 8-16a8 8 0 0 0-8-8z" fill="#fff"/><circle cx="9" cy="8" r="3" fill="#17b8c4"/></svg>
      <p class="address">Haldenweg 14/b/2<br>8020 Lindau<br>Austria</p>
    </div>
    <div class="contact-row phone">
      <svg width="20" height="20" viewBox="0 0 20 20"><path d="M4 1l4 4-2 3c1 3 3 5 6 6l3-2 4 4-3 3C8 19 1 12 1 4z" fill="#fff"/></svg>
      <span>+43 6801527409</span>
    </div>
    <div class="contact-row email">
      <svg width="20" height="20" viewBox="0 0 20 20"><circle cx="10" cy="10" r="8" fill="none" stroke="#fff" stroke-width="2"/><circle cx="10" cy="10" r="3.5" fill="none" stroke="#fff" stroke-width="2"/><path d="M13.5 7v5c0 2 3 2 3 0" fill="none" stroke="#fff" stroke-width="2"/></svg>
      <span>m.berger@lumevaresearch.com</span>
    </div>
  </div>
</footer>
<p class="copyright abs">
  <svg width="16" height="16" viewBox="0 0 16 16"><circle cx="8" cy="8" r="7" fill="none" stroke="#fff" stroke-width="1.4"/><path d="M10.5 6a3 3 0 1 0 0 4" fill="none" stroke="#fff" stroke-width="1.4"/></svg>
  2017 - CORVANE - All rights reserved.
</p>

</body>
</html>
```